I'd like a business card that makes my company, Fenwright Marsh Associates Ltd stand out from the normal financial & IT services sector . It would be great to have a card that a potential client will think "wow" this is out of the norm , I'll give these guys a call. My business aims to provide consultancy services for financial and IT institutions but I'm looking to provide a newer approach that fits into today's social media rather than the standard "big 4" approach. My business helps companies assess their internal issues and aims to solve issues via business process re-engineering. The final design should have a balance of the maturity of the financial & IT sector with the fresh approach of the thriving social media sector

Target Market(s)

Business Managers and Directors, technical Managers and directors. Aged between 20 and 60 that handle project budgets

Industry/Entity Type

Financial

Requirements
Must have
• Must incorporate company logo currently being designed
Should not have
• No old-style fonts please.

```html
<!DOCTYPE html>
<html lang="en">
<head>
<meta charset="utf-8">
<title>Fenwright Marsh Associates Ltd — Business Card</title>
<link rel="stylesheet" href="https://fonts.googleapis.com/css2?family=Exo+2:wght@400;500;600;700&display=swap">
<style>
  :root {
    --navy: #33336e;
    --orange: #f58220;
    --paper: #ffffff;
    --paper-shade: #e4e4e6;
    --ink: #2b2b33;
    --stage: #ecebe8;
  }
  * { margin: 0; padding: 0; box-sizing: border-box; }
  html, body {
    width: 1200px; height: 1019px; overflow: hidden;
    background: var(--stage);
    font-family: "Exo 2", sans-serif;
  }
  .business-card {
    position: absolute; left: 150px; top: 250px;
    width: 900px; height: 520px;
    background: var(--paper-shade);
    box-shadow: 0 18px 40px rgba(0,0,0,.18);
    overflow: hidden;
  }
  .card-shapes { position: absolute; inset: 0; }
  .company-name {
    position: absolute; left: 130px; top: 272px;
    color: var(--navy); font-weight: 500;
    letter-spacing: 1.5px; line-height: 1.25;
    font-size: 22px; text-transform: uppercase;
  }
  .company-name .mark {
    display: inline-block; width: 12px; height: 12px;
    background: var(--navy); border-radius: 50%;
    margin-right: 9px; vertical-align: 2px;
  }
  .holder { position: absolute; right: 225px; top: 50px; text-align: right; }
  .holder-name {
    color: var(--orange); font-weight: 700; font-size: 30px;
    letter-spacing: 1px; text-transform: uppercase; line-height: 1.1;
  }
  .holder-role { color: var(--ink); font-size: 19px; font-weight: 500; }
  .contact-list {
    position: absolute; right: 239px; top: 130px;
    list-style: none; text-align: right;
    color: var(--ink); font-size: 14px; line-height: 26px;
  }
  .contact-list li { display: flex; justify-content: flex-end; align-items: center; gap: 10px; white-space: nowrap; }
  .contact-list li:nth-child(2) { padding-right: 12px; }
  .contact-list li:nth-child(3) { padding-right: 25px; }
  .contact-list li:nth-child(4) { padding-right: 37px; }
  .contact-list li:nth-child(5) { padding-right: 50px; }
  .contact-list svg { width: 14px; height: 14px; fill: none; stroke: var(--orange); stroke-width: 2; flex: none; }
  .contact-list svg .solid { fill: var(--orange); stroke: none; }
</style>
</head>
<body>
  <article class="business-card">
    <svg class="card-shapes" viewBox="0 0 900 520" aria-hidden="true">
      <defs>
        <radialGradient id="panel-sheen" cx="0.45" cy="0.35" r="0.8">
          <stop offset="0" stop-color="#ffffff"/>
          <stop offset="1" stop-color="#e9e9ec"/>
        </radialGradient>
      </defs>
      <path class="orange-top" d="M0 0 H160 Q60 60 0 130 Z" fill="var(--orange)"/>
      <path class="navy-band" d="M0 120 Q80 40 200 0 H760 L900 0 V110 L640 520 H0 Z" fill="var(--navy)"/>
      <path class="orange-base" d="M0 360 Q140 470 420 470 L390 520 H0 Z" fill="var(--orange)"/>
      <path class="white-panel" d="M310 30 H740 L540 450 H310 A210 210 0 0 1 310 30 Z" fill="url(#panel-sheen)"/>
    </svg>

    <div class="company-name"><span class="mark"></span>Fenwright Marsh<br>Associates Ltd</div>

    <div class="holder">
      <p class="holder-name">Daniel Whitcombe</p>
      <p class="holder-role">Managing Director</p>
    </div>

    <ul class="contact-list">
      <li>020 555 0148
        <svg viewBox="0 0 16 16"><path class="solid" d="M3 1h3l1 4-2 1a9 9 0 0 0 5 5l1-2 4 1v3a2 2 0 0 1-2 2A13 13 0 0 1 1 3a2 2 0 0 1 2-2z"/></svg></li>
      <li>020 555 0149
        <svg viewBox="0 0 16 16"><rect x="4" y="1" width="8" height="14" rx="1.5"/><line x1="7" y1="12" x2="9" y2="12"/></svg></li>
      <li>hello@fenwrightmarsh.co.uk
        <svg viewBox="0 0 16 16"><rect x="1" y="3" width="14" height="10" rx="1"/><path d="M1 4l7 5 7-5"/></svg></li>
      <li>www.fenwrightmarsh.co.uk
        <svg viewBox="0 0 16 16"><circle cx="8" cy="8" r="6.5"/><path d="M1.5 8h13M8 1.5c3 3.5 3 9.5 0 13M8 1.5c-3 3.5-3 9.5 0 13"/></svg></li>
      <li>14 Harbour Row Leeds LS1 UK
        <svg viewBox="0 0 16 16"><path class="solid" d="M8 1a5 5 0 0 1 5 5c0 4-5 9-5 9S3 10 3 6a5 5 0 0 1 5-5zm0 3a2 2 0 1 0 0 4 2 2 0 0 0 0-4z"/></svg></li>
    </ul>
  </article>
</body>
</html>
```